High end personal training flyer design

I want a flyer designed to be delivered to people's houses to interest them in high end (and, therefore, not cheap) personal training services.

Don't want standard pictures of people exercising, before and afters, etc. More something that will appeal to that more affluent market.

Flexible on size of flyer, but please make sure it is a standard size that I can get printed easily. Would like it not to look like a normal flyer you get through the letterbox, so if any particular sizes, shapes, etc are known to do that, then that would be a good start.

Text on flyer to be as follows:

Is this you:

Live in East Cheshire
Male, aged 30-50
A father
Cash rich, time poor
Find handling high pressure at work comfortable
But have a short fuse out of work – with the wife, kids, life in general, etc
Not happy with the way your body looks and feels
Know exactly what you should do to sort that, but struggling to actually do it for various reasons
Turned off by the standard menu of options for addressing that – gyms, slimming clubs, diets, etc

If so, you may be interested in what I do.

Some would call it Personal Training. Some would call it Coaching. I’m not interested in giving what I do labels.

What I am interested in is providing the best possible service (and results) for my clients – whatever that entails.

I work closely with one or two clients at a time to make sure they get exactly what they need.

If you would like to find out more about this, I usually meet for a coffee and a chat. To see if we both think our working together is a good idea.

No squeeze pages, no countdowns, mailing lists or false scarcity.

No plastering this flyer with ‘Before and afters’ – they are ten a penny and my clients don’t want to have pictures of them in their underwear spread around the local area.

Just give me a call and we’ll go from there.

My number is 07912645320.

Tim

Industry/Entity Type

Training

Requirements
Should not have
• Generic before and after or exercise type pictures

```html
<!DOCTYPE html>
<html lang="en">
<head>
<meta charset="utf-8">
<title>Is This You? – Personal Training Flyer</title>
<link rel="stylesheet" href="https://fonts.googleapis.com/css2?family=Anton&family=Oswald:wght@400;500;700&family=Lato:wght@400;700&family=Roboto+Condensed:wght@400;700&display=swap">
<style>
  :root {
    --backdrop: #8e8e8e;
    --navy: #1b2a3a;
    --navy-deep: #0f1822;
    --red: #e8302c;
    --red-dark: #b81f1c;
    --blue: #1e5fae;
    --blue-deep: #0d2d63;
    --graphite: #2b2b2b;
    --steel: #9a9a9a;
    --sky: #cfe3f7;
    --sky-light: #eef5fd;
    --white: #ffffff;
    --ink: #222222;
  }
  * { margin: 0; padding: 0; box-sizing: border-box; }
  html, body { width: 900px; height: 1200px; overflow: hidden; background: var(--backdrop); }
  .canvas { position: relative; width: 900px; height: 1200px; overflow: hidden; }
  .flyer-shapes { position: absolute; left: 0; top: 0; }
  .text { position: absolute; }

  .headline {
    left: 65px; top: 70px; width: 772px; text-align: center;
    font-family: "Anton", sans-serif; font-size: 128px; line-height: 1;
    letter-spacing: 4px; color: var(--white);
  }
  .headline .accent { color: var(--red); }

  .live-in {
    left: 90px; top: 240px; font-family: "Oswald", sans-serif; font-weight: 700;
    font-size: 70px; line-height: 1; color: var(--white);
  }
  .location {
    left: 88px; top: 352px; font-family: "Roboto Condensed", sans-serif; font-weight: 700;
    font-size: 36px; line-height: 1; color: var(--white);
  }
  .role {
    left: 90px; top: 420px; font-family: "Roboto Condensed", sans-serif;
    font-size: 50px; line-height: 1; color: var(--ink);
  }
  .role-sub {
    left: 90px; top: 478px; font-family: "Roboto Condensed", sans-serif;
    font-size: 25px; line-height: 1; color: var(--white);
  }

  .profile-copy {
    left: 90px; top: 740px; width: 242px; font-family: "Lato", sans-serif;
    font-size: 13.6px; line-height: 1.3; color: var(--white); text-align: justify;
    hyphens: auto;
  }
  .call-cta {
    left: 92px; top: 974px; font-family: "Oswald", sans-serif; font-weight: 500;
    font-size: 27px; line-height: 1; color: var(--red);
  }
  .call-number {
    left: 92px; top: 1010px; font-family: "Oswald", sans-serif; font-weight: 500;
    font-size: 23px; line-height: 1; letter-spacing: 9px; color: var(--white);
  }
  .contact-line {
    left: 92px; font-family: "Lato", sans-serif; font-size: 13px; color: var(--white);
    display: flex; align-items: center; gap: 6px;
  }
  .contact-web { top: 1086px; }
  .contact-mail { top: 1106px; }

  .brand {
    left: 530px; top: 764px; display: flex; align-items: center; gap: 10px;
    font-family: "Oswald", sans-serif; font-weight: 700; font-size: 28px; line-height: 1;
    color: var(--red); white-space: nowrap;
  }
  .brand-dot { width: 16px; height: 16px; border-radius: 50%; background: var(--red); }

  .offer-lead {
    right: 80px; top: 846px; text-align: right; font-family: "Oswald", sans-serif; font-weight: 500;
    font-size: 23px; line-height: 1; color: var(--white);
  }
  .offer-title {
    right: 80px; top: 878px; text-align: right; font-family: "Roboto Condensed", sans-serif;
    font-size: 46px; line-height: 1; color: var(--white);
  }
  .offer-copy {
    left: 434px; top: 944px; width: 384px; font-family: "Lato", sans-serif;
    font-size: 12.8px; line-height: 1.3; color: var(--ink); text-align: justify;
    text-align-last: right; hyphens: auto;
  }
</style>
</head>
<body>
<main class="canvas">
  <svg class="flyer-shapes" width="900" height="1200" viewBox="0 0 900 1200">
    <defs>
      <linearGradient id="header-fill" x1="0" y1="0" x2="1" y2="1">
        <stop offset="0" stop-color="#2a3c50"/>
        <stop offset="1" stop-color="#0f1822"/>
      </linearGradient>
      <linearGradient id="column-fill" x1="0" y1="0" x2="1" y2="1">
        <stop offset="0" stop-color="#6e6e6e"/>
        <stop offset="1" stop-color="#3c3c3c"/>
      </linearGradient>
      <linearGradient id="photo-fill" x1="0" y1="0" x2="1" y2="1">
        <stop offset="0" stop-color="#b9b9b9"/>
        <stop offset="0.5" stop-color="#5a5a5a"/>
        <stop offset="1" stop-color="#d8d8d8"/>
      </linearGradient>
      <linearGradient id="panel-blue" x1="0" y1="0" x2="1" y2="1">
        <stop offset="0" stop-color="#2a72c6"/>
        <stop offset="1" stop-color="#0a2452"/>
      </linearGradient>
      <linearGradient id="dark-fill" x1="0" y1="0" x2="0" y2="1">
        <stop offset="0" stop-color="#555555"/>
        <stop offset="1" stop-color="#1f1f1f"/>
      </linearGradient>
      <radialGradient id="sky-fill" cx="0.3" cy="0.4" r="0.9">
        <stop offset="0" stop-color="#ffffff"/>
        <stop offset="1" stop-color="#a9cdf0"/>
      </radialGradient>
      <linearGradient id="band-blue" x1="0" y1="0" x2="1" y2="0">
        <stop offset="0" stop-color="#0d2d63"/>
        <stop offset="1" stop-color="#1e5fae"/>
      </linearGradient>
      <radialGradient id="watch-fill" cx="0.4" cy="0.4" r="0.6">
        <stop offset="0" stop-color="#f2f2f2"/>
        <stop offset="1" stop-color="#6f6f6f"/>
      </radialGradient>
    </defs>

    <rect class="flyer-base" x="65" y="58" width="772" height="1084" fill="var(--graphite)"/>

    <rect class="header-band" x="65" y="58" width="772" height="170" fill="url(#header-fill)"/>

    <polygon class="column-backdrop" points="65,228 330,228 462,748 65,748" fill="url(#column-fill)"/>

    <polygon class="portrait" role="img" aria-label="Black and white photograph of a bald older man with head bowed, dissolving into dust"
      points="330,228 837,228 837,560 462,748" fill="url(#photo-fill)"/>

    <polygon class="sky-panel" points="462,748 837,560 837,1142 385,1142" fill="url(#sky-fill)"/>

    <polyline points="462,748 837,560" fill="none" stroke="#d9d9d9" stroke-width="4"/>

    <polygon class="box-live" points="65,232 325,232 345,330 65,330" fill="var(--red)"/>
    <rect x="65" y="330" width="282" height="4" fill="#d6d6d6"/>
    <polygon class="box-location" points="65,338 350,338 366,408 65,408" fill="url(#band-blue)"/>
    <rect x="65" y="408" width="303" height="4" fill="#d6d6d6"/>
    <polygon class="box-role" points="65,415 368,415 392,510 65,510" fill="var(--red)"/>
    <rect x="65" y="510" width="330" height="4" fill="#d6d6d6"/>

    <polygon class="watch-panel" points="65,520 396,520 462,740 65,540" fill="url(#panel-blue)"/>
    <ellipse class="watch" role="img" aria-label="Silver pocket watch" cx="278" cy="607" rx="34" ry="46" fill="url(#watch-fill)"/>

    <polygon points="65,545 462,745 65,590" fill="var(--red)"/>
    <polygon points="65,592 462,746 65,615" fill="#c8c8c8"/>
    <polygon points="65,618 462,747 65,650" fill="var(--red-dark)"/>
    <polygon points="65,652 462,748 65,668" fill="#e25f5b"/>

    <polygon class="info-panel" points="65,672 462,748 393,1100 65,1100" fill="url(#dark-fill)"/>

    <polygon class="footer-band" points="65,1076 398,1076 385,1142 65,1142" fill="var(--blue)"/>
    <polyline points="462,748 385,1142" fill="none" stroke="var(--red)" stroke-width="4"/>
    <polyline points="398,1076 385,1142" fill="none" stroke="#e6e6e6" stroke-width="3"/>

    <polygon class="offer-band" points="432,838 837,838 837,930 414,930" fill="var(--red)"/>

    <polygon points="392,1120 837,1120 837,1142 388,1142" fill="var(--red)"/>
    <polygon points="700,1122 837,1118 837,1142 680,1142" fill="#1a1a1a"/>
  </svg>

  <h1 class="text headline">IS THIS <span class="accent">YOU?</span></h1>

  <div class="text live-in">LIVE IN</div>
  <div class="text location">East Cheshire</div>
  <div class="text role">A FATHER</div>
  <div class="text role-sub">CASH RICH, TIME POOR</div>

  <p class="text profile-copy" lang="en">Find handling high pressure at work comfortable but have a short fuse out of work – with the wife, kids, life in general, etc Not happy with the way your body looks and feels. Know exactly what you should do to sort that, but struggling to actually do it for various reasons Turned off by the standard menu of options for addressing that – gyms, slimming clubs, diets, etc.</p>

  <div class="text call-cta">Just give me A Call</div>
  <div class="text call-number">07912645320</div>

  <div class="text contact-line contact-web">
    <svg width="10" height="10" viewBox="0 0 10 10" aria-hidden="true"><path d="M2 1 L4 3 L3 4 Q4 6 6 7 L7 6 L9 8 L8 9 Q3 9 1 2 Z" fill="#fff"/></svg>
    www.ironvalecoaching.co.uk
  </div>
  <div class="text contact-line contact-mail">
    <svg width="10" height="8" viewBox="0 0 10 8" aria-hidden="true"><rect x="0.5" y="0.5" width="9" height="7" fill="none" stroke="#fff"/><path d="M0.5 0.5 L5 4.5 L9.5 0.5" fill="none" stroke="#fff"/></svg>
    tim@ironvalecoaching.co.uk
  </div>

  <div class="text brand"><span class="brand-dot"></span>IRONVALE COACHING</div>

  <div class="text offer-lead">If so, you may be interested</div>
  <div class="text offer-title">in what I do?</div>

  <p class="text offer-copy" lang="en">Some would call it Personal Training. Some would call it Coaching. I’m not interested in giving what I do labels. What I am interested in is providing the best possible service (and results) for my clients – whatever that entails. I work closely with one or two clients at a time to make sure they get exactly what they need. If you would like to find out more about this, I usually meet for a coffee and a chat. To see if we both think our working together is a good idea. No squeeze pages, no countdowns, mailing lists or false scarcity.</p>
</main>
</body>
</html>
```